Make a medical leaflet for my patients undergoing ankle blocks

I have a very boring text only leaflet I would like to turn into a professional appealing medical leaflet to give to my patients. I would like to get this onto two pages of a4 if possible and its intended for electronic distribution mainly.
This will be for patients so it must be professional.
It must also contain a copyright logo on it and my name near the start (Dr Tobias Wendell) so my colleagues can't use it easily.
Target Market(s)
Patients undergoing surgery
Industry/Entity Type
Medical
Font styles to use
Other font styles liked:
- no idea, you tell me
Requirements
Must have
- the information contained on the attachment
- look professional
- a copyright on it
Nice to have
- the ashbury clinic logo
Should not have
- Any spelling, grammatical or linguistic errors
- Any font less than size 12

```html
<!DOCTYPE html>
<html lang="en">
<head>
<meta charset="utf-8">
<title>Ankle block – patient leaflet</title>
<link rel="stylesheet" href="https://fonts.googleapis.com/css2?family=Lato:wght@400;700;900&display=swap">
<style>
:root{
  --backdrop:#c4966a;
  --page:#1f5b9b;
  --teal:#62c6bc;
  --teal-soft:#6fc3c9;
  --teal-deep:#3fb0a8;
  --ink:#ffffff;
  --corner:#ffffff;
  --brand:#3a3a66;
  --wave:rgba(125,205,245,.42);
}
*{margin:0;padding:0;box-sizing:border-box}
html,body{width:1200px;height:874px;overflow:hidden}
body{background:var(--backdrop);font-family:'Lato',sans-serif;color:var(--ink);position:relative}
.page{position:absolute;top:64px;width:514px;height:722px;background:var(--page);box-shadow:0 4px 10px rgba(0,0,0,.35);overflow:hidden}
.page--front{left:62px}
.page--back{left:614px}
.abs{position:absolute}
.corner{position:absolute;top:0;left:0}
.brand{position:absolute;color:var(--brand);font-weight:400;text-align:center;line-height:1.25;white-space:nowrap}
.brand--front{left:350px;top:20px;width:154px;font-size:12.5px}
.brand--front .brand__sub{font-size:7px}
.brand--back{left:384px;top:14px;width:124px;font-size:9.5px}
.brand--back .brand__sub{font-size:5.5px}
.brand__rule{display:block;height:1px;background:var(--brand);margin:3px 6px}
.wave-area{position:absolute}
.wave-area--front{left:400px;top:400px;width:114px;height:270px;background:linear-gradient(160deg,rgba(125,205,245,0) 0%,var(--wave) 55%,rgba(125,205,245,0) 100%);border-radius:60% 0 0 60%}
.wave-area--back{left:320px;top:0;width:194px;height:360px;background:linear-gradient(200deg,rgba(125,205,245,0) 10%,var(--wave) 50%,rgba(125,205,245,0) 95%);border-radius:0 0 0 80%}
.title{left:38px;top:18px;font-size:41px;font-weight:900;color:var(--teal);letter-spacing:-.5px;line-height:1.1}
.copyright{left:42px;top:70px;font-size:10px;color:var(--teal-deep)}
.intro{font-size:10px;font-weight:700;line-height:12.5px}
.intro p+p{margin-top:12px}
.heading{font-size:16px;color:var(--teal-soft);font-weight:400}
.heading::after{content:"";display:block;height:1px;background:var(--teal-soft);opacity:.8;margin-top:4px}
.benefits{list-style:none;left:36px;top:301px;width:460px}
.benefits li{position:relative;padding-left:26px;font-size:11.6px;font-weight:700;line-height:14.5px;margin-bottom:5px}
.benefits li::before{content:"";position:absolute;left:2px;top:1px;border-left:10px solid var(--ink);border-top:6px solid transparent;border-bottom:6px solid transparent}
.lead{left:38px;top:454px;font-size:10px;font-weight:700}
.risk{left:36px;width:440px;font-size:10px;line-height:10.5px}
.risk__label{position:absolute;left:0;top:0;width:80px;color:var(--teal-soft);font-weight:700}
.risk__body{margin-left:83px}
.options{left:166px;top:606px;font-size:10px;line-height:10.5px}
.footnote{left:34px;top:658px;width:350px;font-size:10px;line-height:10.5px;color:var(--teal-soft)}
.clinic{left:410px;top:650px;width:96px;text-align:center;font-size:11px;font-weight:400;line-height:14px;color:#dfe7f0}
.clinic__dot{display:block;width:8px;height:8px;border-radius:50%;background:#dfe7f0;margin:0 auto 5px}
.h-big{left:40px;top:11px;width:200px;font-size:24px;font-weight:700;color:var(--teal)}
.h-big::after{content:"";display:block;height:1px;background:var(--teal-soft);margin-top:8px}
.sub{left:40px;font-size:11.5px;font-weight:700}
.points{list-style:none;left:40px;width:460px}
.points li{position:relative;padding-left:14px;font-size:10px;line-height:13px}
.points li::before{content:"";position:absolute;left:1px;top:3px;border-left:5px solid var(--ink);border-top:3.5px solid transparent;border-bottom:3.5px solid transparent}
.note{left:45px;top:287px;width:420px;font-size:10px;line-height:10.5px;color:var(--teal-soft)}
.h-mid{left:39px;width:203px}
.col{font-size:9.8px;line-height:12.1px;top:361px}
.closing{left:37px;top:645px;width:440px;font-size:10px;font-weight:700;line-height:12px}
</style>
</head>
<body>

<section class="page page--front">
  <div class="wave-area wave-area--front" role="img" aria-label="Decorative flowing line pattern"></div>
  <svg class="corner" width="514" height="72" aria-hidden="true"><polygon points="274,0 318,72 514,72 514,0" fill="var(--corner)"/></svg>
  <div class="brand brand--front">Riverside Crown Hospital<span class="brand__rule"></span><span class="brand__sub">part of Meridian Health UK</span></div>

  <h1 class="abs title">Ankle block</h1>
  <div class="abs copyright">© Dr Tobias Wendell</div>

  <div class="abs intro" style="left:34px;top:101px;width:226px">
    <p>You are scheduled to have surgery on your foot. It is my normal practice to offer and perform (with your consent) an ankle block. This is an optional injection of numbing liquid to the nerves which supply your foot. The ankle block can be performed when you are awake, sedated or under general anaesthesia.</p>
    <p>The ankle block can be combined with a general anaesthetic and with sedation. It can also be used to allow surgery to be performed with you wide awake in certain cases.</p>
  </div>
  <div class="abs intro" style="left:286px;top:103px;width:186px">
    <p>Having or not having an ankle block does not change the pre operative fasting guidelines you have been given.</p>
    <p>There is a fee for performing an ankle block. Please consult my initial introductory email and terms of business for details</p>
  </div>

  <h2 class="abs heading" style="left:35px;top:262px;width:203px">What are the benefits</h2>
  <ul class="abs benefits">
    <li>Excellent pain relief - usually 10 - 14 hours (and rarely 24 - 48 hours)</li>
    <li>Avoiding traditional painkillers which resulting in less post operative nausea and vomiting</li>
    <li>The option to avoid a general anaesthetic (if you wish)</li>
    <li>A faster recovery from the general anaesthetic</li>
    <li>Certain surgery requires an overnight stay in hospital without an ankle block</li>
  </ul>

  <h2 class="abs heading" style="left:36px;top:415px;width:203px">What are the risks?</h2>
  <p class="abs lead">As with all injections, there is the risk of bruising, bleeding and infection.</p>

  <div class="abs risk" style="top:475px">
    <div class="risk__label">Nerve Damage</div>
    <div class="risk__body">Occurs 1 in 5000 nerve blocks.<br>Creates an area of numbness or weakness/paralysis in some / all the foot.<br>Majority of nerve injuries will heal themselves within a year<br>There is no treatment to fix it<br>If the block has not worn off after 72 hours please let me know.</div>
  </div>
  <div class="abs risk" style="top:532px">
    <div class="risk__label">Failure</div>
    <div class="risk__body">The success rate with ankle blocks is 98 - 99%<br>Some blocks will fail, partially or totally.<br>If total failure, I will discuss repeating the block with your consent.</div>
  </div>
  <div class="abs risk" style="top:580px">
    <div class="risk__label">Pain during<br>operation</div>
    <div class="risk__body">If you choose to have wide awake surgery or surgery under sedation<br>The surgery will stop and I will discuss three options with you</div>
  </div>
  <div class="abs options">- more numbing liquid to be injected by the surgeon<br>- more sedation / painkiller<br>- having a general anaesthetic</div>

  <p class="abs footnote">If you decide to undergo surgery awake or sedated, there is a risk you will need to have a general anaesthetic if you feel pain. This is why the starvation instructions of awake surgery and general anaesthesia are the same.</p>

  <div class="abs clinic"><span class="clinic__dot"></span>The Ashbury<br>Clinic</div>
</section>

<section class="page page--back">
  <div class="wave-area wave-area--back" role="img" aria-label="Decorative flowing line pattern"></div>
  <svg class="corner" width="514" height="56" aria-hidden="true"><polygon points="342,0 378,56 514,56 514,0" fill="var(--corner)"/></svg>
  <div class="brand brand--back">Riverside Crown Hospital<span class="brand__rule"></span><span class="brand__sub">part of Meridian Health UK</span></div>

  <h1 class="abs h-big">How is it done</h1>

  <h3 class="abs sub" style="top:78px">If you choose awake surgery or surgery with sedation -</h3>
  <ul class="abs points" style="top:100px">
    <li>Numbing liquid is injected around the nerves which supply your foot.</li>
    <li>The ankle block takes 5 - 10 minutes to perform and requires 4 - 5 injections</li>
    <li>Approximately 10 - 20 minutes to make your foot numb to pain</li>
    <li>I will check the ankle block is working before we start surgery using cold spray</li>
    <li>Sensations of touch, pressure, vibration and movement will still be felt</li>
    <li>I will use a screen so you can't see the surgery (unless you would like to see)</li>
    <li>Some patients bring headphones to block out the noise of the operation.</li>
  </ul>

  <h3 class="abs sub" style="top:205px">If you choose a General anaesthetic -</h3>
  <ul class="abs points" style="top:229px">
    <li>I will perform the ankle block after I start the general anaesthetic.</li>
    <li>You should wake up from your surgery with a comfortable and numb foot/feet</li>
    <li>If you wake in pain, we can repeat the ankle block or provide traditional painkillers</li>
  </ul>

  <p class="abs note">Whatever you choose, there will be a cannula placed in your hand and heart and oxygen monitoring throughout.</p>

  <h2 class="abs heading h-mid" style="top:324px">After surgery</h2>
  <p class="abs col" style="left:42px;width:208px">You will go to the recovery area and then onto the ward when you are ready. It will be difficult to walk while the block is working so physiotherapists will help you first walk. If you need crutches they will teach you how to use them. Your foot will be numb and so you will not feel where your foot is in relation to nearby objects. As a result, it is easy to knock your foot. Please take extra care while your foot is still numb. As the block wears off, the foot may feel slightly painful, tingly or hot. At this point you should take your painkillers I have prescribed. Depending on your medical</p>
  <p class="abs col" style="left:277px;width:202px;top:362px">history you will have up to three painkillers. I would suggest to start with all three. You will also have an anti - sickness prescribed if one of the painkillers (typically codeine or morphine) makes you feel sick. Occasionally (1 - 2%), pain when the block wears off will be severe. In this case contact your surgeon's secretary. We can use stronger pain medication, but there will be charge in writing and getting the private prescription to you (please see my terms of business) via courier.</p>

  <h2 class="abs heading h-mid" style="top:538px">The alternative</h2>
  <ul class="abs points" style="top:577px">
    <li>If you do not have an ankle block your surgery can still proceed.</li>
    <li>Post operative pain can be managed with traditional painkillers.</li>
    <li>However, you are more likely to need an overnight stay or feel sick after the anaesthetic.</li>
  </ul>

  <p class="abs closing">If you have any further questions about an ankle block I will see you the day of your surgery. Alternatively, you can request the following optional services (as mentioned in my terms of business).</p>
</section>

</body>
</html>
```